oneness poster

a clean, elegant, simple text poster as follows (with some sort of glow or background consistent with the message:
MANIFESTO OF QUIET RIVERS

1. I am part of the world. The world is not outside of me, and I am not outside of the world. The world is in me, and I am in the world.

2. I am part of nature, and nature is part of me. I am what I am in my communication and communion with all living things. I am an irreducible and coherent whole with the web of life on the planet.

3. I am part of society, and society is part of me. I am what I am in my communication and communion with my fellow humans. I am an irreducible and coherent whole with the community of humans on the planet.

4. I am more than a skin-and-bone material organism: my body, and its cells and organs are manifestations of what is truly me: a self-sustaining, self-evolving dynamic system arising, persisting and evolving in interaction with everything around me.

5. I am one of the highest, most evolved manifestations of the drive toward coherence and wholeness in the universe. All systems drive toward coherence and wholeness in interaction with all other systems, and my essence is this cosmic drive. It is the same essence, the same spirit that is inherent in all the things that arise and evolve in nature, whether on this planet or elsewhere in the infinite reaches of space and time.

6. There are no absolute boundaries and divisions in this world, only transition points where one set of relations yields prevalence to another. In me, in this self-maintaining and self-evolving coherence- and wholeness-oriented system, the relations that integrate the cells and organs of my body are prevalent. Beyond my body other relations gain prevalence: those that drive toward coherence and wholeness in society and in nature.

7. The separate identity I attach to other humans and other things is but a convenient convention that facilitates my interaction with them. My family and my community are just as much “me” as the organs of my body. My body and mind, my family and my community, are interacting and interpenetrating, variously prevalent elements in the network of relations that encompasses all things in nature and the human world.

8. The whole gamut of concepts and ideas that separates my identity, or the identity of any person or community, from the identity of other persons and communities are manifestations of this convenient but arbitrary convention. There are only gradients distinguishing individuals from each other and from their environment and no real divisions and boundaries. There are no “others” in the world: we are all living systems and we are all part of each other.

9. Attempting to maintain the system I know as “me” through ruthless competition with the system I know as “you” is a grave mistake: it could damage the integrity of the embracing whole that frames both your life and mine. I cannot preserve my own life and wholeness by damaging that whole, even if damaging a part of it seems to bring me short-term advantage. When I harm you, or anyone else around me, I harm myself.

10. Collaboration, not competition, is the royal road to the wholeness that hallmarks healthy systems in the world. Collaboration calls for empathy and solidarity, and ultimately for love. I do not and cannot love myself if I do not love you and others around me: we are part of the same whole and so are part of each other.

11. The idea of “self-defense” even of “national defense,” needs to be rethought. Patriotism if it aims to eliminate adversaries by force, and heroism even in the well-meaning execution of that aim, are mistaken aspirations. A patriot and a hero who brandishes a sword or a gun is an enemy also to himself. Every weapon intended to hurt or kill is a danger to all. Comprehension, conciliation and forgiveness are not signs of weakness; they are signs of courage.

12. “The good” for me and for every person in the world is not the possession and accumulation of personal wealth. Wealth, in money or in any material resource, is but a means for maintaining myself in my environment. As exclusively mine, it commandeers part of the resources that all things need to share if they are to live and to thrive. Exclusive wealth is a threat to all people in the human community. And because I am a part of this community, in the final count it is a threat also to me, and to all who hold it.

13. Beyond the sacred whole we recognize as the world in its totality, only life and its development have what philosophers call intrinsic value; all other things have merely instrumental value: value insofar as they add to or enhance intrinsic value. Material things in the world, and the energies and substances they harbor or generate, have value only if and insofar they contribute to life and wellbeing in the web of life on this Earth.

14. Every healthy person has pleasure in giving: it is a higher pleasure than having. I am healthy and whole when I value giving over having. The true measure of my accomplishment and excellence is my readiness to give. Not the amount of what I give is the measure of my accomplishment and excellence, but the relation between what I give, and what my family and I need to live and to thrive.

15. A community that values giving over having is a community of healthy people, oriented toward thriving through empathy, solidarity, and love among its members. Sharing enhances the community of life, while possessing and accumulating creates demarcation, invites competition, and fuels envy. The share-society is the norm for all the communities of life on the planet; the have-society is typical only of modern-day humanity, and it is an aberration.
.

16. I acknowledge my role and responsibility in evolving a planetary consciousness in me, and by example in others around me. I have been part of the aberration of human consciousness in the modern age, and now wish to become part of the evolution that overcomes the aberration and heals the wounds inflicted by it. This is my right as well as my duty, as a conscious member of a conscious species on a precious and now critically endangered planet.

• MANIFESTO OF QUIET RIVERS

.

• a very very simple glow in the background or other look consistent with the all-is-one (OM) message. A strong, almost spirtual feel.
• no flowery designs, no distractions. Nothing cute.

```html
<!DOCTYPE html>
<html lang="en">
<head>
<meta charset="utf-8">
<title>Manifesto of Quiet Rivers</title>
<link href="https://fonts.googleapis.com/css2?family=Raleway:wght@300&family=EB+Garamond:wght@400&family=Oswald:wght@600&family=Orbitron:wght@800&display=swap" rel="stylesheet">
<style>
  :root {
    --bg-deep: #2a10b8;
    --bg-mid: #2f3fe0;
    --bg-low: #5a2fc8;
    --title: #e8894e;
    --numeral: #c9ec6e;
    --keyword: #ff2fd0;
    --panel: rgba(190, 196, 232, 0.78);
    --panel-edge: rgba(255, 255, 255, 0.55);
    --ink: #1d1a3a;
  }
  * { box-sizing: border-box; margin: 0; padding: 0; }
  html, body { width: 800px; height: 1200px; overflow: hidden; }
  body {
    position: relative;
    background:
      radial-gradient(ellipse 520px 420px at 400px 330px, rgba(120,150,255,0.55), transparent 70%),
      repeating-conic-gradient(from 0deg at 400px 330px, rgba(255,255,255,0.06) 0deg 6deg, transparent 6deg 14deg),
      linear-gradient(180deg, var(--bg-deep) 0%, var(--bg-mid) 35%, var(--bg-low) 100%);
    font-family: "EB Garamond", Georgia, serif;
    color: var(--ink);
  }
  .poster-title {
    position: absolute; top: 18px; left: 0; width: 800px;
    text-align: center;
    font-family: "Raleway", "Helvetica Neue", sans-serif;
    font-weight: 300; font-size: 47px; letter-spacing: 1px;
    color: var(--title);
  }
  .poster-title span {
    border-bottom: 2px solid var(--title); padding-bottom: 2px;
  }
  .word-field {
    position: absolute; left: 110px; top: 88px; width: 590px; height: 470px;
    border-radius: 50%;
    background:
      radial-gradient(circle at 35% 40%, rgba(190,255,120,0.55), transparent 45%),
      radial-gradient(circle at 70% 35%, rgba(120,230,255,0.55), transparent 45%),
      radial-gradient(circle at 75% 80%, rgba(255,130,60,0.45), transparent 40%),
      radial-gradient(ellipse at center, rgba(70,40,200,0.9), rgba(60,60,220,0) 72%);
    filter: blur(2px);
  }
  .column {
    position: absolute; top: 566px;
    display: flex; flex-direction: column; gap: 8px;
  }
  .column--left { left: 35px; width: 360px; }
  .column--right { left: 418px; width: 352px; }
  .tenet {
    display: grid; grid-template-columns: 34px 1fr; align-items: start;
    background: var(--panel);
    border: 1px solid var(--panel-edge);
    border-radius: 3px;
    box-shadow: 0 0 10px 3px rgba(170,180,255,0.55);
    padding: 4px 7px 4px 4px;
  }
  .tenet__num {
    font-family: "Oswald", "Arial Narrow", sans-serif; font-weight: 600;
    font-size: 34px; line-height: 34px; color: var(--numeral);
    text-shadow: 0 0 3px rgba(255,255,255,0.6);
  }
  .tenet__text { font-size: 8.7px; line-height: 10.2px; padding-top: 1px; text-align: justify; }
  .kw {
    font-family: "Orbitron", "Arial Black", sans-serif; font-weight: 800;
    font-size: 7px; text-transform: uppercase; color: var(--keyword);
  }
  .footer-rule {
    position: absolute; left: 195px; top: 1177px; width: 410px;
    border-top: 1px dotted rgba(255,255,255,0.6);
  }
</style>
</head>
<body>
  <h1 class="poster-title"><span>MANIFESTO of QUIET RIVERS</span></h1>
  <div class="word-field" role="img" aria-label="Glowing typographic cloud of words: world, nature, society, identity, integrity, interaction, empathy, solidarity, wellbeing, sharing, conciliation, love"></div>

  <section class="column column--left">
    <article class="tenet"><div class="tenet__num">1.</div><p class="tenet__text">I am part of the <span class="kw">world</span>. The world is not outside of me, and I am not outside of the world. The world is in me, and I am in the world.</p></article>
    <article class="tenet"><div class="tenet__num">2.</div><p class="tenet__text">I am part of <span class="kw">nature</span>, and nature is part of me. I am what I am in my communication and communion with all living things. I am an irreducible and coherent whole with the web of life on the planet.</p></article>
    <article class="tenet"><div class="tenet__num">3.</div><p class="tenet__text">I am part of <span class="kw">society</span>, and society is part of me. I am what I am in my communication and communion with my fellow humans. I am an irreducible and coherent whole with the community of humans on the planet.</p></article>
    <article class="tenet"><div class="tenet__num">4.</div><p class="tenet__text">I am more than a skin-and-bone material organism: my body, and its cells and organs are manifestations of what is truly me: a self-sustaining, self-evolving <span class="kw">dynamic</span> system arising, persisting and evolving in interaction with everything around me.</p></article>
    <article class="tenet"><div class="tenet__num">5.</div><p class="tenet__text">I am one of the highest, most evolved manifestations of the drive toward <span class="kw">coherence</span> and wholeness in the universe. All systems drive toward coherence and wholeness in interaction with all other systems, and my essence is this cosmic drive. It is the same essence, the same spirit that is inherent in all the things that arise and evolve in nature, whether on this planet or elsewhere in the infinite reaches of space and time.</p></article>
    <article class="tenet"><div class="tenet__num">6.</div><p class="tenet__text">There are no absolute boundaries and divisions in this world, only <span class="kw">transition</span> points where one set of relations yields prevalence to another. In me, in this self-maintaining and self-evolving coherence- and wholeness-oriented system, the relations that integrate the cells and organs of my body are prevalent. Beyond my body other relations gain prevalence: those that drive toward coherence and wholeness in society and in nature.</p></article>
    <article class="tenet"><div class="tenet__num">7.</div><p class="tenet__text">The separate <span class="kw">identity</span> I attach to other humans and other things is but a convenient convention that facilitates my interaction with them. My family and my community are just as much “me” as the organs of my body. My body and mind, my family and my community, are interacting and interpenetrating, variously prevalent elements in the network of relations that encompasses all things in nature and the human world.</p></article>
    <article class="tenet"><div class="tenet__num">8.</div><p class="tenet__text">The whole gamut of concepts and ideas that separates my identity, or the identity of any person or <span class="kw">community</span>, from the identity of other persons and communities are manifestations of this convenient but arbitrary convention. There are only gradients distinguishing individuals from each other and from their environment and no real divisions and boundaries. There are no “others” in the world: we are all living systems and we are all part of each other.</p></article>
    <article class="tenet"><div class="tenet__num">9.</div><p class="tenet__text">Attempting to maintain the system I know as “me” through ruthless competition with the system I know as “you” is a grave mistake: it could damage the <span class="kw">integrity</span> of the embracing whole that frames both your life and mine. I cannot preserve my own life and wholeness by damaging that whole, even if damaging a part of it seems to bring me short-term advantage. When I harm you, or anyone else around me, I harm myself.</p></article>
  </section>

  <section class="column column--right">
    <article class="tenet"><div class="tenet__num">10.</div><p class="tenet__text"><span class="kw">Collaboration</span>, not competition, is the royal road to the wholeness that hallmarks healthy systems in the world. Collaboration calls for empathy and solidarity, and ultimately for love. I do not and cannot love myself if I do not love you and others around me: we are part of the same whole and so are part of each other.</p></article>
    <article class="tenet"><div class="tenet__num">11.</div><p class="tenet__text">The idea of “self-defense” even of “national defense,” needs to be rethought. Patriotism if it aims to eliminate adversaries by force, and heroism even in the well-meaning execution of that aim, are mistaken aspirations. A patriot and a hero who brandishes a sword or a gun is an enemy also to himself. Every weapon intended to hurt or kill is a danger to all. Comprehension, <span class="kw">conciliation</span> and forgiveness are not signs of weakness; they are signs of courage.</p></article>
    <article class="tenet"><div class="tenet__num">12.</div><p class="tenet__text">“The good” for me and for every person in the world is not the possession and accumulation of personal wealth. Wealth, in money or in any material resource, is but a means for maintaining myself in my environment. As exclusively mine, it commandeers part of the resources that all things need to share if they are to live and to thrive. Exclusive wealth is a threat to all people in the <span class="kw">human community</span>. And because I am a part of this community, in the final count it is a threat also to me, and to all who hold it.</p></article>
    <article class="tenet"><div class="tenet__num">13.</div><p class="tenet__text">Beyond the sacred whole we recognize as the world in its totality, only life and its development have what philosophers call intrinsic value; all other things have merely instrumental value: value insofar as they add to or enhance intrinsic value. Material things in the world, and the energies and substances they harbor or generate, have value only if and insofar they contribute to life and <span class="kw">wellbeing</span> in the web of life on this Earth.</p></article>
    <article class="tenet"><div class="tenet__num">14.</div><p class="tenet__text">Every healthy person has pleasure in giving: it is a higher pleasure than having. I am healthy and whole when I value giving over having. The true measure of my accomplishment and excellence is my readiness <span class="kw">to give</span>. Not the amount of what I give is the measure of my accomplishment and excellence, but the relation between what I give, and what my family and I need to live and to thrive.</p></article>
    <article class="tenet"><div class="tenet__num">15.</div><p class="tenet__text">A community that values giving over having is a community of healthy people, oriented toward thriving through <span class="kw">empathy, solidarity, and love</span> among its members. Sharing enhances the community of life, while possessing and accumulating creates demarcation, invites competition, and fuels envy. The share-society is the norm for all the communities of life on the planet; the have-society is typical only of modern-day humanity, and it is an aberration.</p></article>
    <article class="tenet"><div class="tenet__num">16.</div><p class="tenet__text">I acknowledge my role and <span class="kw">responsibility</span> in evolving a planetary consciousness in me, and by example in others around me. I have been part of the aberration of human consciousness in the modern age, and now wish to become part of the evolution that overcomes the aberration and heals the wounds inflicted by it. This is my right as well as my duty, as a conscious member of a conscious species on a precious and now critically endangered planet.</p></article>
  </section>

  <div class="footer-rule"></div>
</body>
</html>
```